2 Funky Pages + EASY stock logo = Construction Website

We would like a funky new website - Just 2 pages - to promote our project management company. A logo is also needed, but we'll provide a stock image which just needs a colour change a text added.

Here are the instructions:

"Fair Tally Homes"

#logo
The one I'd like is attached. Please change font and positioning of text though.

Tagline is "Don't be normal - Be clever"

#Colour combo
756897 Wood Veneer
D5D6D2 sand dollar
353C3F charcoal
962715 brick red

#Home - Page 1

Our cost-price home build service will save you thousands.
No, seriously - Here's how we do it (button)

- Pay what the home building companies do.
- FTH will manage the entire project.
- Use Keystonecraft Guaranteed builders and materials.
- Tender for the best industry rates.
- Get a full budget calculated for the build.
- Avoid inflated 'Fixed-price' builds.
See how it works (button)

Contact Us: 0800 615 278
enquire - Name, Phone, email, comment - SEND

#How it works - Page 2

Traditional fixed price contracts are popular because it means that any risk of unexpected problems is carried by the home builder, but the builder will generally load the price about 10 times above the actual risk carried.

It's like an over-priced insurance policy, on steroids.

Clever people do things differently.

Here's how a cost-price build works...

1) Tell us what you want to build. Dream home, townhouse, investment property, whatever.

2) We'll put a design together for you, or you can choose from a bunch of plans we've already got.

3) We'll give you a conservative price estimate.

4) We finish tweaking your plans, then send them out to our network of more than 200 builders, subcontractors and tradesmen.

5) We collect the quotes, pick the best prices, and finalise your budget. Now you buy us beer, cause you've finally realised how much you're saving.

6) Tell your friends how awesome we are, while we lodge your building consent application with Council.

7) We coordinate the builders and subbies (look, you're already speaking trade-talk) from start to finish. You pay the cost price on their work each month.

We're happy to talk numbers and give you an estimate.

Contact Us: 0800 615 278

Reason: I have seen some great design elements, but need them to come together in one site design. Also, there appears to be less attention paid to the second page design ('how it works') than is necessary... There is no viable contender there yet, compared with the great home page submissions. I've also added some further info to the brief, and note that many submissions have ignored the colour combo I've requested.

Industry/Entity Type

Construction

Number of Pages Required

2 page

Requirements
Must have
• Keystonecrafter logo (small)
• Colour combo described in brief.
Nice to have
• I've attached a stock image I like, but it's certainly not essential. I do like images with clear backgrounds though - they tend to produce a crisp looking site.
• There is a wider image similar to this, available on Pixel Vault, but Sketch Hive won't let me attach it.
Should not have
• Photos of cheesy American faces.

```html
<!DOCTYPE html>
<html lang="en">
<head>
<meta charset="utf-8">
<title>Fair Tally Homes – Home</title>
<link rel="stylesheet" href="https://fonts.googleapis.com/css2?family=Arimo:ital,wght@0,400;0,700;1,400&family=Didact+Gothic&display=swap">
<style>
  :root {
    --wood-veneer: #756897;
    --sand-dollar: #D5D6D2;
    --charcoal: #353C3F;
    --brick-red: #962715;
    --ink: #2f3436;
    --panel-top: #b3b6b3;
    --panel-bottom: #d0d1cd;
    --white: #ffffff;
  }
  * { box-sizing: border-box; margin: 0; padding: 0; }
  html, body { width: 1200px; height: 750px; overflow: hidden; }
  body {
    position: relative;
    background: var(--sand-dollar);
    font-family: "Arimo", Arial, sans-serif;
    color: var(--ink);
  }

  /* Header */
  .site-header {
    position: absolute; left: 0; top: 0; width: 1200px; height: 192px;
    background: var(--sand-dollar);
    border-bottom: 2px solid var(--charcoal);
  }
  .brand {
    position: absolute; left: 40px; top: 40px; width: 170px;
    display: flex; align-items: center; gap: 12px;
  }
  .brand-mark { width: 34px; height: 34px; background: var(--brick-red); flex: none; }
  .brand-name {
    font-family: "Arimo", Arial, sans-serif; font-weight: 700;
    font-size: 24px; line-height: 28px; color: var(--brick-red);
  }
  .tagline {
    position: absolute; left: 341px; top: 86px;
    font-family: "Didact Gothic", "Century Gothic", sans-serif;
    font-variant: small-caps; font-size: 26px; letter-spacing: 3px;
    color: var(--ink);
  }
  .contact-line {
    position: absolute; right: 19px; top: 15px;
    font-style: italic; font-size: 15px; letter-spacing: 0.5px;
  }

  /* Main panel */
  .main-panel {
    position: absolute; left: 0; top: 192px; width: 1200px; height: 490px;
    background: linear-gradient(to bottom, var(--panel-top), var(--panel-bottom));
  }
  .intro { position: absolute; left: 19px; top: 13px; width: 700px; }
  .intro-headline { font-style: italic; font-size: 18px; letter-spacing: 0.5px; }
  .label-small { font-style: italic; font-size: 14px; letter-spacing: 0.5px; }
  .no-seriously { margin-top: 22px; }
  .btn {
    display: inline-block; background: var(--brick-red); color: var(--white);
    border-radius: 6px; font-size: 14px; text-align: center;
    text-decoration: none; line-height: 30px; height: 31px;
  }
  .btn-how-we-do-it { width: 162px; margin-top: 3px; }
  .benefits { list-style: none; margin-top: 46px; font-size: 14px; line-height: 18px; letter-spacing: 0.3px; }
  .see-label { margin-top: 18px; font-size: 14px; }
  .btn-how-it-works { width: 125px; margin-top: 3px; }

  /* Enquiry form */
  .enquiry { position: absolute; left: 826px; top: 13px; width: 356px; }
  .enquiry-title { font-size: 18px; letter-spacing: 0.5px; font-weight: 400; }
  .field-row { display: flex; align-items: center; justify-content: space-between; height: 31px; margin-top: 7px; }
  .field-row:first-of-type { margin-top: 12px; }
  .field-label { font-style: italic; font-size: 14px; letter-spacing: 0.5px; }
  .field-input {
    width: 281px; height: 31px; border: 1.5px solid var(--charcoal);
    border-radius: 6px; background: var(--sand-dollar);
  }
  .comment-label { display: block; margin-top: 18px; }
  .comment-input {
    display: block; width: 354px; height: 71px; margin-top: 2px;
    border: 1.5px solid var(--charcoal); border-radius: 8px; background: var(--sand-dollar);
  }
  .btn-send {
    position: absolute; right: 0; top: 277px; width: 125px;
    border: none; font-family: inherit;
  }

  /* Footer */
  .site-footer {
    position: absolute; left: 0; top: 682px; width: 1200px; height: 68px;
    background: var(--charcoal); color: var(--white);
  }
  .member-badge {
    position: absolute; left: 19px; top: 6px; width: 44px; height: 55px;
    background: var(--white);
  }
  .copyright {
    position: absolute; left: 547px; top: 24px; font-style: italic; font-size: 11px;
  }
  .footer-nav { position: absolute; right: 20px; top: 24px; font-size: 11px; }
  .footer-nav a { color: var(--white); text-decoration: none; }
</style>
</head>
<body>
  <header class="site-header">
    <div class="brand">
      <span class="brand-mark"></span>
      <span class="brand-name">Fair Tally Homes</span>
    </div>
    <p class="tagline">Don’t be normal - Be clever</p>
    <p class="contact-line">Contact Us: 0800 615 278</p>
  </header>

  <main class="main-panel" role="img" aria-label="Faint architectural plan drawing behind the content">
    <section class="intro">
      <h1 class="intro-headline" style="font-weight:400">Our cost-price home build service will save you thousands.</h1>
      <p class="label-small no-seriously">No, seriously:</p>
      <a class="btn btn-how-we-do-it" href="#">Here’s how we do it</a>
      <ul class="benefits">
        <li>- Pay what the home building companies do.</li>
        <li>- FTH will manage the entire project.</li>
        <li>- Use Keystonecraft Guaranteed builders and materials.</li>
        <li>- Tender for the best industry rates.</li>
        <li>- Get a full budget calculated for the build.</li>
        <li>- Avoid inflated 'Fixed-price' builds.</li>
      </ul>
      <p class="see-label">See:</p>
      <a class="btn btn-how-it-works" href="#">How it works</a>
    </section>

    <form class="enquiry">
      <h2 class="enquiry-title">SEND ENQUIRY</h2>
      <div class="field-row"><span class="field-label">Name:</span><span class="field-input"></span></div>
      <div class="field-row"><span class="field-label">Phone:</span><span class="field-input"></span></div>
      <div class="field-row"><span class="field-label">Email:</span><span class="field-input"></span></div>
      <span class="field-label comment-label">Comment:</span>
      <span class="comment-input"></span>
      <span class="btn btn-send">SEND</span>
    </form>
  </main>

  <footer class="site-footer">
    <div class="member-badge" role="img" aria-label="Registered builders membership badge"></div>
    <p class="copyright">© Fair Tally Homes 2016</p>
    <nav class="footer-nav"><a href="#">Home</a> &nbsp;|&nbsp; <a href="#">How it Works</a></nav>
  </footer>
</body>
</html>
```